Wine Label Design for the red wine named “Amber Over Stone” or “A/S”

Create an elegant yet simple (less is more) label for a red, full-bodied wine from a family-owned Herzegovinian vineyard by the river with 9 names. You can use elements such as the Calopteryx virgo, possibly the river shape, and ensure a coherent storytelling of the unique vineyard’s locality and meticulous, hand-picked grape cultivation.
Let’s craft a label that is not just seen, but is experienced and remembered.

Target Market(s)

Wine lovers that appreciate high quality wines

Industry/Entity Type

Wine, Family owned small producer

Requirements
Must have
• Name A/S, front and back label. Premium feel, uniqueness. Simple but interesting.
Nice to have
• Please see the images below as an idea of various directions. I am also leaning to embossed image on the label
Should not have
• Should not be overcrowded with text, too many images and objects

```html
<!DOCTYPE html>
<html lang="en">
<head>
<meta charset="utf-8">
<title>Amber Over Stone — Front Label</title>
<link rel="stylesheet" href="https://fonts.googleapis.com/css2?family=Barlow+Condensed:wght@300;400&display=swap">
<style>
  :root {
    --backdrop: #1d1b1a;
    --label-black: #121212;
    --band-black: #0c0c0c;
    --stripe-gloss: #2a2a2a;
    --ink-silver: #d6d3cf;
    --ink-muted: #8e8b88;
  }
  * { margin: 0; padding: 0; box-sizing: border-box; }
  html, body {
    width: 1200px;
    height: 607px;
    overflow: hidden;
    background: var(--backdrop);
  }
  .canvas {
    position: relative;
    width: 1200px;
    height: 607px;
    display: flex;
    align-items: center;
    justify-content: center;
  }
  .label {
    position: relative;
    width: 300px;
    height: 552px;
    display: flex;
    flex-direction: column;
    font-family: "Barlow Condensed", sans-serif;
    color: var(--ink-silver);
  }
  .label-main {
    position: relative;
    height: 452px;
    background: var(--label-black);
  }
  .house-mark {
    position: absolute;
    top: 14px;
    right: 22px;
    font-weight: 400;
    font-size: 22px;
    letter-spacing: 2px;
    color: var(--ink-silver);
  }
  .wine-name-large {
    position: absolute;
    top: 190px;
    left: 0;
    width: 100%;
    text-align: center;
    font-weight: 300;
    font-size: 96px;
    letter-spacing: 4px;
    line-height: 1;
    color: var(--ink-muted);
  }
  .vintage {
    position: absolute;
    bottom: 12px;
    left: 0;
    width: 100%;
    text-align: center;
    font-weight: 400;
    font-size: 11px;
    letter-spacing: 1.5px;
    color: var(--ink-muted);
  }
  .label-divider {
    height: 26px;
    background: linear-gradient(to bottom,
      var(--band-black) 0, var(--band-black) 4px,
      var(--stripe-gloss) 4px, var(--stripe-gloss) 10px,
      var(--band-black) 10px, var(--band-black) 18px,
      var(--stripe-gloss) 18px, var(--stripe-gloss) 22px,
      var(--band-black) 22px);
  }
  .label-band {
    flex: 1;
    background: var(--label-black);
    display: flex;
    align-items: center;
    justify-content: center;
  }
  .wine-name {
    font-weight: 400;
    font-size: 15px;
    letter-spacing: 2.6px;
    text-transform: uppercase;
    color: var(--ink-silver);
  }
</style>
</head>
<body>
  <main class="canvas">
    <article class="label">
      <section class="label-main">
        <div class="house-mark">A/S</div>
        <div class="wine-name-large">A/S</div>
        <div class="vintage">2022</div>
      </section>
      <div class="label-divider"></div>
      <section class="label-band">
        <h1 class="wine-name">Amber Over Stone</h1>
      </section>
    </article>
  </main>
</body>
</html>
```